Quiet River Psalter Reflections for Every Season of Long Waiting

This is not an Eastern meditation method. No images or themes from guru style or Eastern meditations from Hinduism or Buddhism will work. This is a Biblical Christian-based method. Some sort of Divine Light from Heaven may be the look. Some "ancient scroll" for the title to be written in may work.

```html
<!DOCTYPE html>
<html lang="en">
<head>
<meta charset="utf-8">
<title>Quiet River Psalter — Book Cover</title>
<link href="https://fonts.googleapis.com/css2?family=Tinos:wght@400;700&display=swap" rel="stylesheet">
<style>
  :root {
    --night: #1f1918;
    --umber: #4a2e22;
    --ember: #b8702f;
    --amber: #e0a35a;
    --dawn: #f7ead6;
    --gold: #a8863a;
    --title: #ffffff;
    --ink: #1d1814;
  }
  html, body {
    margin: 0;
    padding: 0;
    width: 849px;
    height: 1200px;
    overflow: hidden;
    background: var(--night);
  }
  .cover {
    position: relative;
    width: 849px;
    height: 1200px;
    overflow: hidden;
    font-family: "Tinos", "Times New Roman", serif;
  }
  .cover-art {
    position: absolute;
    inset: 0;
    background:
      radial-gradient(ellipse 260px 300px at 90px 760px, rgba(255,248,235,0.95), rgba(255,240,215,0) 100%),
      radial-gradient(ellipse 320px 260px at 250px 700px, rgba(240,150,80,0.75), rgba(240,150,80,0) 100%),
      radial-gradient(ellipse 420px 330px at 600px 720px, rgba(200,120,60,0.8), rgba(200,120,60,0) 100%),
      radial-gradient(ellipse 500px 260px at 330px 1030px, rgba(250,236,215,0.9), rgba(250,236,215,0) 100%),
      linear-gradient(180deg, var(--night) 0%, #2b211e 22%, var(--umber) 38%, var(--ember) 58%, var(--amber) 75%, var(--dawn) 90%, #d8b48c 100%);
  }
  .author {
    position: absolute;
    top: 50px;
    left: 0;
    width: 849px;
    text-align: center;
    margin: 0;
    font-weight: 700;
    font-size: 48px;
    line-height: 1.2;
    color: var(--gold);
    letter-spacing: 0.5px;
  }
  .title {
    margin: 0;
    font-weight: 400;
    color: var(--title);
  }
  .title span {
    position: absolute;
    line-height: 1;
    white-space: nowrap;
    text-shadow: 4px 5px 4px rgba(20,10,5,0.85);
  }
  .title .initial { left: 92px;  top: 90px;  font-size: 400px; }
  .title .word-1  { left: 388px; top: 133px; font-size: 192px; }
  .title .word-2  { left: 392px; top: 302px; font-size: 180px; }
  .title .word-3  { left: 392px; top: 494px; font-size: 150px; }
  .subtitle {
    position: absolute;
    left: 104px;
    top: 940px;
    margin: 0;
    font-weight: 400;
    font-size: 60px;
    line-height: 67px;
    color: var(--ink);
    letter-spacing: 0.5px;
  }
</style>
</head>
<body>
  <main class="cover">
    <div class="cover-art" role="img" aria-label="Sunrise seen through an open stone tomb, three crosses on a distant hill and folded linen cloth on the rock"></div>
    <p class="author">Thomas Everly</p>
    <h1 class="title">
      <span class="initial">Q</span>
      <span class="word-1">uiet</span>
      <span class="word-2">River</span>
      <span class="word-3">Psalter</span>
    </h1>
    <p class="subtitle">Reflections<br>For Every Season of<br>Long Waiting</p>
  </main>
</body>
</html>
```